Brindle Works Australia Website

Brindle Works Australia (BWA) is a Industrial, Mining & Transport Services provider in Australia. We require a website that is both pc and mobile freindly. The website will be used to both present our company services and give us exposure in a crowded market. The main page of the website will have a snapshot of who BWA is and its from this page that the user can click to enter the area of interest ie. Industrial, Mining and Transport. A disticted logo can be used to indicate the area in question.<br/>Within the industrial, Mining and the Transport services pages will need list and description of services that are provided, current customer lists and news pages.<br/>The website will need a contacts page so prospective customers can get in contact with BWA.<br/>The website design will require a user freindly back end so future updates and ammendments can be carriedout by less experienced people within the BWA business.

Target Market(s)

Industrial, Mining and Transport Services provider markets

Coding

Number of Pages Required

5+ page

Font styles to use
Sans Serif

Colors
00a990

Requirements
Must have
• Ability to build servises with in services. because the main service area is only the main service with in each service group there is alot of smaller services / tasks.
• Key wording for easy seach engine capabilities. The website will need to be search engine freindly.

```html
<!DOCTYPE html>
<html lang="en">
<head>
<meta charset="utf-8">
<title>Brindle Works Australia – Mining &amp; Transport Services</title>
<link href="https://fonts.googleapis.com/css2?family=Montserrat:wght@400;500;600;700&family=Poppins:wght@400;500;600;700&display=swap" rel="stylesheet">
<style>
:root{
  --green:#2d6b3b;
  --green-dark:#275c33;
  --ink:#222;
  --text:#444;
  --muted:#666;
  --bar:#f1f1f1;
  --card:#f2f2f2;
  --line:#cfcfcf;
  --white:#fff;
  --black:#111;
}
*{margin:0;padding:0;box-sizing:border-box}
html,body{width:1200px;height:3717px;overflow:hidden}
body{position:relative;background:var(--white);font-family:"Montserrat",sans-serif;color:var(--text)}
.abs{position:absolute}
.ph{position:absolute}
/* top bar */
.topbar{left:0;top:0;width:1200px;height:32px;background:var(--bar);font-size:12px;color:var(--text)}
.topbar b{color:var(--green);font-weight:600}
.topbar .phone{left:75px;top:9px}
.topbar .email{left:552px;top:9px}
.topbar .social{right:0;top:0;width:255px;height:32px;background:var(--green-dark);clip-path:polygon(28px 0,100% 0,100% 100%,0 100%)}
.topbar .social span{position:absolute;top:9px;width:14px;height:14px;border-radius:50%;background:var(--white);opacity:.9}
.topbar .sep{position:absolute;top:0;width:1px;height:32px;background:rgba(255,255,255,.25)}
/* header */
.brand{left:75px;top:58px}
.brand .name{font-family:"Montserrat",sans-serif;font-weight:700;font-size:25px;color:var(--green);letter-spacing:.5px;line-height:1}
.brand .name small{display:block;font-size:14px;margin-top:4px;letter-spacing:.6px}
.brand .tag{font-size:10px;font-weight:700;color:var(--ink);margin-top:8px;letter-spacing:.3px}
.nav{top:82px;font-size:13px;color:var(--ink)}
.nav.active{color:var(--green)}
.nav-dot{left:555px;top:63px;width:14px;height:10px;border-radius:50%;background:var(--green)}
.search{left:1114px;top:82px}
/* hero */
.hero-bg{left:0;top:151px;width:1200px;height:508px;background:linear-gradient(160deg,#3f5a2e 0%,#5d7440 40%,#8a8c77 75%,#b9b7ad 100%)}
.hero-fade{left:0;top:659px;width:1200px;height:110px;background:linear-gradient(#e6e4df,#fff)}
.hero-machine{left:680px;top:222px;width:520px;height:520px;border-radius:40px 0 0 40px;background:linear-gradient(160deg,#e6b62a 0%,#d9a51e 45%,#3d3d3d 80%,#2a2a2a 100%);opacity:.92}
.hero h1{left:115px;top:340px;font-family:"Poppins",sans-serif;font-weight:600;font-size:31px;line-height:37px;color:var(--white)}
.hero p{left:117px;top:425px;width:330px;font-size:12px;line-height:15px;color:var(--white)}
.btn{display:flex;align-items:center;justify-content:center;background:var(--green);color:var(--white);font-size:13px;position:absolute}
.hero .btn{left:114px;top:472px;width:180px;height:41px;justify-content:flex-start;padding-left:53px}
.btn .arr{position:absolute;right:12px;top:50%;margin-top:-7px}
.slide-arrow{top:380px;width:26px;height:26px;border:1.5px solid rgba(255,255,255,.6);border-radius:50%}
/* about */
.about-photo{left:89px;top:764px;width:502px;height:390px;border-radius:6px;background:radial-gradient(ellipse at 45% 45%,#8a8c86 0%,#777a73 45%,#a6ab9e 80%,#f4f4f2 100%)}
.about-line{left:584px;top:857px;width:62px;height:3px;background:var(--green)}
.h2{font-family:"Poppins",sans-serif;font-weight:500;color:var(--ink)}
.about-title{left:659px;top:840px;font-size:29px}
.about-text{left:649px;top:893px;width:445px;font-size:12px;line-height:15px;color:var(--muted)}
.about-text p{margin-bottom:15px}
.about .btn{left:652px;top:1090px;width:186px;height:45px}
/* section titles */
.sec-title{width:1200px;left:0;text-align:center;font-size:29px}
.orn{left:540px;width:120px;height:14px}
/* service cards */
.svc{top:1315px;width:339px;height:397px;background:var(--card)}
.svc .img{position:absolute;left:8px;top:8px;width:323px;height:203px}
.svc .icon{position:absolute;left:150px;top:189px;width:40px;height:40px;border-radius:50%;background:var(--white)}
.svc .icon i{position:absolute;left:12px;top:12px;width:16px;height:16px;border-radius:3px;background:var(--ink)}
.svc h3{position:absolute;left:0;top:232px;width:100%;text-align:center;font-family:"Poppins",sans-serif;font-weight:500;font-size:17px;color:var(--ink)}
.svc p{position:absolute;left:40px;top:286px;width:259px;text-align:center;font-size:12px;line-height:15px;color:var(--muted)}
.svc .go{position:absolute;left:158px;top:357px}
.svc.on{background:var(--green)}
.svc.on h3,.svc.on p{color:var(--white)}
.svc.on .icon{background:var(--white)}
.svc.on .icon i{background:var(--green)}
/* projects */
.filters{top:1825px;font-size:12px;font-weight:600;color:var(--ink)}
.filters.on{color:var(--green)}
.proj-frame{left:307px;top:1874px;width:281px;height:494px;background:var(--green)}
.proj-inner{left:316px;top:1883px;width:263px;height:476px;background:linear-gradient(#2f3a44,#3a3a36 60%,#4a3f33)}
.proj-caption{left:326px;top:2253px;color:var(--white)}
.proj-caption h4{font-size:14px;font-weight:700;margin-bottom:14px}
.proj-caption p{font-size:12px;line-height:15px;width:230px}
.view{left:509px;width:188px;height:45px}
/* news */
.news{top:2546px;width:339px;height:353px;background:var(--card)}
.news .img{position:absolute;left:9px;top:9px;width:321px;height:201px}
.news .date{position:absolute;left:16px;top:158px;width:44px;height:40px;background:var(--green);color:var(--white);font-size:12px;font-weight:700;text-align:center;line-height:15px;padding-top:5px}
.news h4{position:absolute;left:16px;top:224px;font-size:12px;font-weight:600;color:var(--ink)}
.news p{position:absolute;left:16px;top:257px;width:310px;font-size:12px;line-height:15px;color:var(--muted)}
.news .more{position:absolute;left:16px;top:323px;font-size:12px;color:var(--muted);display:flex;align-items:center;gap:5px}
/* contact */
.contact-bg{left:0;top:3000px;width:1200px;height:360px;background:linear-gradient(#fff,#f3f3f1 40%,#ecebe7)}
.contact-title{font-size:32px;top:3026px}
.field{position:absolute;border:1px solid #bdbdbd;background:rgba(255,255,255,.6);font-size:12px;color:var(--muted);padding:13px 12px}
.contact .btn{left:609px;top:3199px;width:262px;height:43px}
/* footer */
.footer{left:0;top:3332px;width:1200px;height:310px}
.f-brand{left:75px;top:3487px}
.f-brand .name{font-weight:700;font-size:25px;color:var(--white);line-height:1}
.f-brand .name small{display:block;font-size:14px;margin-top:4px;letter-spacing:.6px}
.f-brand .tag{font-size:10px;font-weight:700;color:var(--white);margin-top:8px}
.f-head{top:3422px;font-size:13px;font-weight:600;color:var(--white)}
.f-head:after{content:"";display:block;width:32px;height:1px;background:var(--white);margin-top:8px}
.f-links{left:437px;top:3474px;list-style:none;font-size:13px;color:var(--white)}
.f-links li{height:22.5px;padding-left:20px;position:relative}
.f-links li:before{content:"";position:absolute;left:0;top:7px;width:4px;height:4px;border-radius:50%;background:var(--white)}
.f-info{color:var(--white);font-size:12px;line-height:17px}
.f-info svg{position:absolute;left:-24px;top:2px}
.news-in{left:886px;top:3513px;width:240px;height:39px;background:var(--white);font-size:12px;color:var(--ink);padding:12px 13px}
.news-btn{left:886px;top:3560px;width:240px;height:40px;background:var(--black);color:var(--white);font-size:12px;display:flex;align-items:center;justify-content:center}
.copy{left:75px;top:3664px;font-size:13px;color:var(--ink)}
.soc{top:3654px;width:34px;height:34px;border-radius:50%;background:var(--green-dark)}
</style>
</head>
<body>

<!-- top bar -->
<div class="abs topbar">
  <div class="abs phone"><b>Phone:</b> +61 (0)400 555 018</div>
  <div class="abs email"><b>Email:</b> info@brindleworks.com.au</div>
  <div class="abs social">
    <span style="left:43px"></span><i class="sep" style="left:70px"></i>
    <span style="left:90px"></span><i class="sep" style="left:117px"></i>
    <span style="left:133px"></span><i class="sep" style="left:160px"></i>
    <span style="left:176px"></span>
  </div>
</div>

<!-- header -->
<div class="abs brand">
  <div class="name">BWA<small>BRINDLE WORKS AUSTRALIA</small></div>
  <div class="tag">MINING AND TRANSPORT SERVICES</div>
</div>
<span class="abs nav-dot"></span>
<div class="abs nav active" style="left:542px">Home</div>
<div class="abs nav" style="left:619px">About Us</div>
<div class="abs nav" style="left:713px">Our Services</div>
<div class="abs nav" style="left:824px">Projects</div>
<div class="abs nav" style="left:910px">Latest News</div>
<div class="abs nav" style="left:1023px">Contact Us</div>
<svg class="abs search" width="14" height="14" viewBox="0 0 14 14"><circle cx="6" cy="6" r="4.5" fill="none" stroke="#222" stroke-width="1.6"/><line x1="9.3" y1="9.3" x2="13" y2="13" stroke="#222" stroke-width="1.6"/></svg>

<!-- hero -->
<section class="hero">
  <div class="ph hero-bg" role="img" aria-label="Green hillside behind a mining site"></div>
  <div class="ph hero-fade"></div>
  <div class="ph hero-machine" role="img" aria-label="Yellow wheel loader with raised bucket"></div>
  <span class="abs slide-arrow" style="left:40px"></span>
  <span class="abs slide-arrow" style="left:1147px"></span>
  <h1 class="abs">Mining &amp; Transport<br>Services provider in Australia</h1>
  <p class="abs">Lorem Ipsum is simply dummy text of the printing typesetting industry has the industry's .</p>
  <a class="btn">Read More
    <svg class="arr" width="14" height="14" viewBox="0 0 14 14"><circle cx="7" cy="7" r="6" fill="none" stroke="#fff" stroke-width="1.2"/><path d="M4 7h6M7.5 4.5 10 7l-2.5 2.5" fill="none" stroke="#fff" stroke-width="1.2"/></svg>
  </a>
</section>

<!-- about -->
<section class="about">
  <div class="ph about-photo" role="img" aria-label="Aerial photograph of a quarry and processing site"></div>
  <span class="abs about-line"></span>
  <h2 class="abs h2 about-title">About us</h2>
  <div class="abs about-text">
    <p>Lorem Ipsum is simply dummy text of the printing and typesetting an has been the industry's standard dummy text ever since the 1500s,</p>
    <p>when an unknown printer took a galley of type and scrambled it to make a type specimen book. It has survived not only five centuries but also the leap into electronic typesetting, remaining essentially a unchanged. It was popularised in the 1960s</p>
    <p>with the release of Tessaline sheets containing Lorem Ipsum passages and more recently with desktop publishing software like Quillset Page Maker including versions of Lorem Ipsum.</p>
  </div>
  <a class="btn">Read More</a>
</section>

<!-- services -->
<h2 class="abs h2 sec-title" style="top:1220px">Our Services</h2>
<svg class="abs orn" style="top:1272px" viewBox="0 0 120 14"><line x1="4" y1="7" x2="48" y2="7" stroke="#2d6b3b" stroke-width="1.5"/><circle cx="60" cy="7" r="6" fill="#2d6b3b"/><line x1="72" y1="7" x2="116" y2="7" stroke="#2d6b3b" stroke-width="1.5"/></svg>

<div class="abs svc" style="left:68px">
  <div class="img" role="img" aria-label="Industrial refinery towers under grey sky" style="background:linear-gradient(#8e9191,#5b5e5c 60%,#3a3b39)"></div>
  <span class="icon"><i></i></span>
  <h3>Industrial Services Division</h3>
  <p>BWA Industrial Services Division offers an integrated site service and maintenance of your fixed plant.</p>
  <svg class="go" width="24" height="24" viewBox="0 0 24 24"><circle cx="12" cy="12" r="10.5" fill="none" stroke="#2d6b3b" stroke-width="2"/><path d="M7 12h9M12.5 8l4 4-4 4" fill="none" stroke="#2d6b3b" stroke-width="2"/></svg>
</div>
<div class="abs svc on" style="left:430px">
  <div class="img" role="img" aria-label="Yellow bulldozer on a dirt site" style="background:linear-gradient(#a7abac,#8b8266 55%,#5e5140)"></div>
  <span class="icon"><i></i></span>
  <h3>Mining Services Division</h3>
  <p>BWA Industrial Services Division offers an integrated site service and maintenance of your fixed plant.</p>
  <svg class="go" width="24" height="24" viewBox="0 0 24 24"><circle cx="12" cy="12" r="10.5" fill="none" stroke="#fff" stroke-width="2"/><path d="M7 12h9M12.5 8l4 4-4 4" fill="none" stroke="#fff" stroke-width="2"/></svg>
</div>
<div class="abs svc" style="left:796px">
  <div class="img" role="img" aria-label="Blue truck on a highway at sunset" style="background:linear-gradient(#e8b58a,#c78a68 45%,#3c5068 75%,#6b6b6f)"></div>
  <span class="icon"><i></i></span>
  <h3>BWA Transport Division</h3>
  <p>BWA Industrial Services Division offers an integrated site service and maintenance of your fixed plant.</p>
  <svg class="go" width="24" height="24" viewBox="0 0 24 24"><circle cx="12" cy="12" r="10.5" fill="none" stroke="#2d6b3b" stroke-width="2"/><path d="M7 12h9M12.5 8l4 4-4 4" fill="none" stroke="#2d6b3b" stroke-width="2"/></svg>
</div>

<!-- projects -->
<h2 class="abs h2 sec-title" style="top:1780px">Our Projects</h2>
<div class="abs filters on" style="left:358px">All</div>
<div class="abs filters" style="left:400px">Industrial Services Division</div>
<div class="abs filters" style="left:587px">Mining Services Division</div>
<div class="abs filters" style="left:760px">Transport Division</div>

<div class="ph" role="img" aria-label="Yellow haul truck in an open pit" style="left:0;top:1874px;width:280px;height:235px;background:linear-gradient(#9fa3a4,#7d7a70 55%,#8e8a80)"></div>
<div class="ph" role="img" aria-label="Green diesel generator on grass" style="left:0;top:2133px;width:280px;height:235px;background:linear-gradient(#9ab58a,#2b8a4e 45%,#2f3b34)"></div>
<div class="ph proj-frame"></div>
<div class="ph proj-inner" role="img" aria-label="Concrete batching plant at dusk"></div>
<div class="abs proj-caption">
  <h4>Project Name</h4>
  <p>Lorem Ipsum is simply dummy text imagies typessetting industry.</p>
  <svg style="margin-top:6px" width="16" height="16" viewBox="0 0 16 16"><circle cx="8" cy="8" r="6.5" fill="none" stroke="#fff" stroke-width="1.3"/><path d="M5 8h6M8.5 5.5 11 8l-2.5 2.5" fill="none" stroke="#fff" stroke-width="1.3"/></svg>
</div>
<div class="ph" role="img" aria-label="Excavator and grader moving sand at sunset" style="left:616px;top:1874px;width:280px;height:235px;background:linear-gradient(#7d7a72,#c9a260 55%,#d8b275)"></div>
<div class="ph" role="img" aria-label="Excavator loading a dump truck in a mine" style="left:616px;top:2133px;width:280px;height:235px;background:linear-gradient(#6d6760,#4a423a 55%,#8b6d46)"></div>
<div class="ph" role="img" aria-label="City skyline with twin towers behind a construction yard" style="left:923px;top:1874px;width:277px;height:494px;background:linear-gradient(#a9a59a,#8a8478 40%,#55524c 70%,#3e3c38)"></div>

<a class="btn view" style="top:2401px">View More</a>

<!-- news -->
<h2 class="abs h2 sec-title" style="top:2494px">Latest News</h2>

<div class="abs news" style="left:68px">
  <div class="img" role="img" aria-label="Forklift lifting sacks in a warehouse" style="background:linear-gradient(135deg,#e0dbd0,#c9a13b 55%,#5c4a2a)"></div>
  <div class="date">06<br>Jan</div>
  <h4>What is Lorem Ipsum?</h4>
  <p>Lorem Ipsum is simply dummy text of &nbsp;printing on typesetting an has been the industry's standard dummy text ever since the 1500s,</p>
  <span class="more">Read More <svg width="12" height="12" viewBox="0 0 12 12"><circle cx="6" cy="6" r="5" fill="none" stroke="#2d6b3b" stroke-width="1.2"/><path d="M3.5 6h4.5M6.5 4 8.5 6 6.5 8" fill="none" stroke="#2d6b3b" stroke-width="1.2"/></svg></span>
</div>
<div class="abs news" style="left:434px">
  <div class="img" role="img" aria-label="Wheel loader on a sandy quarry" style="background:linear-gradient(#d1b487,#b99565 55%,#9c7a4f)"></div>
  <div class="date">06<br>Jan</div>
  <h4>What is Lorem Ipsum?</h4>
  <p>Lorem Ipsum is simply dummy text of &nbsp;printing on typesetting an has been the industry's standard dummy text ever since the 1500s,</p>
  <span class="more">Read More <svg width="12" height="12" viewBox="0 0 12 12"><circle cx="6" cy="6" r="5" fill="none" stroke="#2d6b3b" stroke-width="1.2"/><path d="M3.5 6h4.5M6.5 4 8.5 6 6.5 8" fill="none" stroke="#2d6b3b" stroke-width="1.2"/></svg></span>
</div>
<div class="abs news" style="left:796px">
  <div class="img" role="img" aria-label="White trucks lined up by stacked shipping containers" style="background:linear-gradient(#b6444a,#7b3a3e 45%,#485c72 80%,#8f8f8f)"></div>
  <div class="date">06<br>Jan</div>
  <h4>What is Lorem Ipsum?</h4>
  <p>Lorem Ipsum is simply dummy text of &nbsp;printing on typesetting an has been the industry's standard dummy text ever since the 1500s,</p>
  <span class="more">Read More <svg width="12" height="12" viewBox="0 0 12 12"><circle cx="6" cy="6" r="5" fill="none" stroke="#2d6b3b" stroke-width="1.2"/><path d="M3.5 6h4.5M6.5 4 8.5 6 6.5 8" fill="none" stroke="#2d6b3b" stroke-width="1.2"/></svg></span>
</div>

<a class="btn view" style="top:2928px">View More</a>

<!-- quick contact -->
<section class="contact">
  <div class="ph contact-bg" role="img" aria-label="Faint mining site landscape"></div>
  <h2 class="abs h2 sec-title contact-title">Quick Contact</h2>
  <div class="field" style="left:330px;top:3087px;width:263px;height:43px">Name</div>
  <div class="field" style="left:330px;top:3143px;width:263px;height:43px">Phone</div>
  <div class="field" style="left:330px;top:3199px;width:263px;height:43px">Email</div>
  <div class="field" style="left:609px;top:3087px;width:262px;height:99px;padding-top:8px">Message</div>
  <a class="btn">Send</a>
</section>

<!-- footer -->
<svg class="abs footer" viewBox="0 0 1200 310" preserveAspectRatio="none">
  <path d="M0 40 C200 20 420 60 640 34 C840 10 1000 0 1200 4 L1200 310 L0 310Z" fill="#2a6336"/>
  <path d="M0 40 C200 20 420 60 640 34 C840 10 1000 0 1200 4" fill="none" stroke="#1e2a22" stroke-width="5"/>
</svg>
<div class="abs f-brand">
  <div class="name">BWA<small>BRINDLE WORKS AUSTRALIA</small></div>
  <div class="tag">MINING AND TRANSPORT SERVICES</div>
</div>

<div class="abs f-head" style="left:437px">Quick Link</div>
<ul class="abs f-links">
  <li>Home</li><li>About Us</li><li>Our Services</li><li>Projects</li><li>Latest News</li><li>Contact Us</li>
</ul>

<div class="abs f-head" style="left:619px">Contact Info</div>
<div class="abs f-info" style="left:643px;top:3474px">
  <svg width="12" height="14" viewBox="0 0 12 14"><path d="M6 1a4 4 0 0 1 4 4c0 3-4 8-4 8S2 8 2 5a4 4 0 0 1 4-4z" fill="none" stroke="#fff" stroke-width="1.2"/><circle cx="6" cy="5" r="1.4" fill="#fff"/></svg>
  PO Box 1200 Harbourvale<br>WA 6000, Australia
</div>
<div class="abs f-info" style="left:643px;top:3546px">
  <svg width="14" height="12" viewBox="0 0 14 12"><rect x="1" y="3" width="12" height="8" rx="1" fill="none" stroke="#fff" stroke-width="1.1"/><path d="M3 3V1h8v2" fill="none" stroke="#fff" stroke-width="1.1"/></svg>
  +61 (0)400 555 018
</div>
<div class="abs f-info" style="left:643px;top:3570px">
  <svg width="14" height="12" viewBox="0 0 14 12"><rect x="1" y="2" width="12" height="9" fill="none" stroke="#fff" stroke-width="1.1"/><path d="M1 2l6 5 6-5" fill="none" stroke="#fff" stroke-width="1.1"/></svg>
  info@brindleworks.com.au
</div>

<div class="abs f-head" style="left:886px">Join Our Newletter</div>
<div class="abs f-info" style="left:886px;top:3474px;width:240px;line-height:14px">Lorem Ipsum is simply dummy text of the industry's standard.</div>
<div class="abs news-in">Your Email Here</div>
<div class="abs news-btn">Submit</div>

<div class="abs copy">Copyright © 2020 Brindle Works Australia. All Right Reserved</div>
<span class="abs soc" style="left:950px"></span>
<span class="abs soc" style="left:998px"></span>
<span class="abs soc" style="left:1046px"></span>
<span class="abs soc" style="left:1092px"></span>

</body>
</html>
```